Business card for a Exhibition booth fabrication company

Hi. My company would like to change our corporate name card. We are an events and Exhibition stand builder company. We would like our corporate name card to resonate what we do. I need someone to create something unique that relates to the industry that I am in. The graphic designer should be creative to incorporate the elements of my industry and try to blend in well in the design of the card. Our aim is to ensure that we are unique and our card can look different from our competitors.
Updates

The decision maker was very busy and didnt had time to make this decision

Target Market(s)

Marketing and events manager from all companies

Contact Information for Business Card

The business card should have the following details:
Name
Job Title
Email
Website

Colors

Designer to choose colors to be used in the design.

Requirements
Must have
• The card must be look something that is relevant to the service that I am providing. My website is: www.velmora-buildworks.example
• You can see my website to get more information on what service that I am doing
Nice to have
• On the back of my card, I would like to have a globe image with the incorporation of my company logo. This is to indicate that my services can be done in any part of the world.

```html
<!DOCTYPE html>
<html lang="en">
<head>
<meta charset="utf-8">
<title>Velmora Buildworks – Business Card</title>
<link href="https://fonts.googleapis.com/css2?family=Jost:wght@400;500&display=swap" rel="stylesheet">
<style>
  :root {
    --page-bg: #e9eaec;
    --card-white: #ffffff;
    --card-dark: #333333;
    --brand-red: #b3262b;
    --text-light: #f2f2f2;
    --text-ink: #262626;
    --text-grey: #5a5a5a;
    --back-light: #f4f4f4;
    --back-mid: #e8e8e8;
  }
  * { margin: 0; padding: 0; box-sizing: border-box; }
  html, body {
    width: 1200px; height: 900px; overflow: hidden;
    background: var(--page-bg);
    font-family: "Jost", sans-serif;
  }
  .sheet {
    position: relative; width: 1200px; height: 900px;
    display: flex; align-items: center; justify-content: center; gap: 40px;
  }
  .card {
    position: relative; width: 540px; height: 308px; overflow: hidden;
    box-shadow: 0 4px 14px rgba(0,0,0,0.18);
  }

  /* Front */
  .card-front { background: var(--card-dark); }
  .front-identity {
    position: absolute; left: 0; top: 0; width: 198px; height: 100%;
    background: var(--card-white);
  }
  .front-stripe {
    position: absolute; left: 198px; top: 0; width: 9px; height: 100%;
    background: var(--brand-red);
  }
  .brand-name {
    position: absolute; left: 22px; top: 34px;
    display: flex; align-items: center; gap: 10px;
    color: var(--brand-red); font-weight: 500; font-size: 22px; line-height: 1.05;
  }
  .brand-dot {
    width: 26px; height: 26px; border-radius: 50%;
    background: var(--brand-red); flex: none;
  }
  .person {
    position: absolute; left: 0; width: 198px; top: 192px;
    text-align: center; color: var(--brand-red);
    font-size: 31px; line-height: 44px; font-weight: 400;
    white-space: nowrap;
  }
  .contact-list {
    position: absolute; left: 232px; top: 0; width: 300px; height: 100%;
    list-style: none; color: var(--text-light);
  }
  .contact-item {
    position: absolute; left: 0; display: flex; align-items: center; gap: 14px;
    font-size: 17px; white-space: nowrap;
  }
  .contact-item svg { width: 30px; height: 28px; flex: none; stroke: var(--text-light); fill: none; stroke-width: 1.6; }
  .contact-web { top: 167px; }
  .contact-mail { top: 220px; font-size: 16.5px; }
  .contact-phone { top: 258px; gap: 8px; font-size: 15.5px; line-height: 21px; }
  .contact-phone svg { width: 26px; height: 26px; }

  /* Back */
  .card-back {
    background: linear-gradient(180deg, var(--back-light), var(--back-mid));
  }
  .globe-area {
    position: absolute; left: 16px; top: 26px; width: 508px; height: 160px;
    border-radius: 50% 50% 12% 12% / 80% 80% 20% 20%;
    background: radial-gradient(ellipse at 55% 45%, #c8c8c8 0%, #d6d6d6 45%, rgba(232,232,232,0) 75%);
  }
  .back-brand {
    position: absolute; left: 0; width: 100%; top: 216px;
    text-align: center; color: var(--text-grey);
    font-size: 11px; font-weight: 500; letter-spacing: 2.6px; text-transform: uppercase;
  }
  .back-brand .brand-dot { display: inline-block; width: 10px; height: 10px; vertical-align: -1px; margin-right: 6px; }
  .tagline-glow {
    position: absolute; left: 50px; width: 440px; top: 250px; height: 30px;
    background: radial-gradient(ellipse at center, rgba(0,0,0,0.12), rgba(0,0,0,0) 70%);
  }
  .tagline {
    position: absolute; left: 0; width: 100%; top: 250px;
    text-align: center; color: var(--text-ink); font-size: 19px;
  }
</style>
</head>
<body>
<main class="sheet">
  <section class="card card-front" aria-label="Business card front">
    <div class="front-identity">
      <div class="brand-name"><span class="brand-dot"></span><span>Velmora<br>Buildworks</span></div>
      <div class="person">
        <p class="person-name">Dana Kessler</p>
        <p class="person-title">Owner</p>
      </div>
    </div>
    <div class="front-stripe"></div>
    <ul class="contact-list">
      <li class="contact-item contact-web">
        <svg viewBox="0 0 30 28"><rect x="2" y="2" width="26" height="19" rx="1"/><line x1="6" y1="7" x2="24" y2="7"/><line x1="6" y1="11" x2="24" y2="11"/><line x1="6" y1="15" x2="18" y2="15"/><line x1="15" y1="21" x2="15" y2="25"/><line x1="10" y1="25.5" x2="20" y2="25.5"/></svg>
        <span>Velmora-Buildworks.example</span>
      </li>
      <li class="contact-item contact-mail">
        <svg viewBox="0 0 30 28"><path d="M2 11 L15 2 L28 11 V26 H2 Z"/><path d="M2 11 L15 19 L28 11"/><path d="M7 8 V5 H23 V8"/></svg>
        <span>Info@Velmora-Buildworks.example</span>
      </li>
      <li class="contact-item contact-phone">
        <svg viewBox="0 0 26 26"><path d="M6 3 L10 7 L8 10 C9 13 12 16 16 18 L19 16 L23 20 L20 24 C11 22 4 15 2 6 Z"/></svg>
        <span>Singapore Contact: +65 9100 4827<br>Qatar Contact: +974 5521 0936</span>
      </li>
    </ul>
  </section>

  <section class="card card-back" aria-label="Business card back">
    <div class="globe-area" role="img" aria-label="Grey world map arching across the card, showing global reach"></div>
    <p class="back-brand"><span class="brand-dot"></span>Velmora Buildworks</p>
    <div class="tagline-glow"></div>
    <p class="tagline">Turning Concepts Into Built Spaces</p>
  </section>
</main>
</body>
</html>
```